Designing a Chocolate Bar's Package

We are a chocolate manufacturing company located in Lebanon. We produce chocolate on a wholesale level, and we are planning a new line of production at the moment.
We intend to be make small chocolate bars (about 30g) similar to the "Varsen Cascade" bar with several flavors. 2 flavors have been decided so far (Mint flavored dark chocolate and Plain dark chocolate).
The packaging material will be similar to varsen's package as well. It won't be a carton box. It'll be some sort of paper wrapping the entire bar. So I am looking for a design that has a unique and cool front and back look.
If only one design is to be prepared, please choose either the mint's flavor or the plain dark chocolate, and prepare the design accordingly.
Updates
Project Deadline Extended
Reason: I still have some time to begin the production. The new deadline,therefore, is the end of this month.
Target Market(s)
basically all chocolate lovers...
Industry/Entity Type
It Company
Requirements
Must have
- I will be uploading our logo. Please make sure to use it in the design.

```html
<!DOCTYPE html>
<html lang="en">
<head>
<meta charset="utf-8">
<title>Celvano Plain Dark Chocolate – Wrapper Front and Back</title>
<link rel="stylesheet" href="https://fonts.googleapis.com/css2?family=Almendra:wght@400;700&family=Tinos&family=Kalam:wght@700&display=swap">
<style>
  :root {
    --paper: #ffffff;
    --frame: #000000;
    --wrapper: #fbfa7a;
    --cocoa: #5a2a12;
    --cocoa-soft: #7b4a2a;
    --gold: #f5c400;
    --gold-deep: #c98a1c;
    --band-edge: #7a3f12;
    --tagline: #b88a4a;
    --label: #111111;
  }
  * { margin: 0; padding: 0; box-sizing: border-box; }
  html, body { width: 1200px; height: 846px; overflow: hidden; background: var(--paper); }
  .sheet {
    position: relative;
    width: 1200px;
    height: 846px;
    border: 1px solid var(--frame);
    overflow: hidden;
  }
  .wrappers { position: absolute; left: 0; top: 0; width: 1200px; height: 846px; }
  .wrapper-shape { fill: var(--wrapper); }

  .band {
    position: absolute;
    height: 34px;
    background:
      repeating-linear-gradient(90deg, rgba(90,42,18,0.12) 0 2px, transparent 2px 6px),
      linear-gradient(90deg, var(--band-edge), var(--gold-deep) 20%, var(--gold) 40%, var(--gold) 60%, var(--gold-deep) 80%, var(--band-edge));
  }
  .ornament {
    position: absolute;
    width: 126px;
    border-radius: 40% 40% 30% 30%;
    background: radial-gradient(ellipse at center, rgba(107,51,24,0.55), rgba(107,51,24,0.18) 70%, transparent 100%);
  }

  .brand-name {
    position: absolute;
    width: 382px;
    text-align: center;
    font-family: "Almendra", serif;
    font-weight: 700;
    color: var(--cocoa);
    line-height: 1;
  }
  .tagline {
    position: absolute;
    font-family: "Almendra", serif;
    font-weight: 400;
    font-size: 15px;
    color: var(--tagline);
  }
  .flavour {
    position: absolute;
    width: 382px;
    text-align: center;
    font-family: "Almendra", serif;
    font-weight: 700;
    color: var(--cocoa);
    line-height: 1;
  }
  .product-word {
    position: absolute;
    font-family: "Kalam", cursive;
    font-weight: 700;
    color: var(--gold);
    line-height: 1;
    transform: rotate(-9deg);
    white-space: nowrap;
  }
  .chocolate-photo {
    position: absolute;
    left: 155px; top: 380px; width: 329px; height: 160px;
    background: radial-gradient(ellipse at 45% 45%, #8a6a5c 0%, #5b3a2e 35%, #3e241b 70%, #2a1710 100%);
    overflow: hidden;
  }
  .weight {
    position: absolute;
    width: 382px;
    text-align: center;
    font-family: "Almendra", serif;
    font-weight: 700;
    font-size: 28px;
    color: var(--cocoa);
  }
  .side-label {
    position: absolute;
    top: 788px;
    width: 300px;
    text-align: center;
    font-family: "Tinos", serif;
    font-size: 30px;
    color: var(--label);
  }
</style>
</head>
<body>
<main class="sheet">
  <svg class="wrappers" viewBox="0 0 1240 874" preserveAspectRatio="none" aria-hidden="true">
    <path class="wrapper-shape" d="M135,112 C120,90 100,70 100,55 C140,40 170,30 200,40 C260,55 300,30 350,35 C420,40 470,25 520,40 C545,45 565,40 575,48 C560,70 535,90 530,112 L530,742 C545,760 565,770 575,775 C520,770 470,760 410,768 C350,775 300,762 250,768 C190,775 150,772 105,773 C115,760 130,745 135,742 Z"/>
    <path class="wrapper-shape" transform="translate(575 0)" d="M135,112 C120,90 100,70 100,55 C140,40 170,30 200,40 C260,55 300,30 350,35 C420,40 470,25 520,40 C545,45 565,40 575,48 C560,70 535,90 530,112 L530,742 C545,760 565,770 575,775 C520,770 470,760 410,768 C350,775 300,762 250,768 C190,775 150,772 105,773 C115,760 130,745 135,742 Z"/>
  </svg>

  <!-- Front of wrapper -->
  <section class="wrapper-front">
    <div class="brand-name" style="left:131px; top:140px; font-size:66px;">Celvano</div>
    <div class="tagline" style="left:163px; top:216px;">Quality Chocolate Store</div>

    <div class="band" style="left:131px; top:261px; width:382px;"></div>
    <div class="ornament" role="img" aria-label="Brown swirl flourish ornament" style="left:134px; top:295px; height:44px;"></div>
    <div class="ornament" role="img" aria-label="Brown swirl flourish ornament" style="left:384px; top:295px; height:44px;"></div>

    <div class="flavour" style="left:131px; top:352px; font-size:28px;">plain dark</div>
    <div class="chocolate-photo" role="img" aria-label="Photo of swirled melted dark chocolate">
      <div class="product-word" style="left:82px; top:64px; font-size:42px;">chocolate</div>
    </div>

    <div class="ornament" role="img" aria-label="Brown swirl flourish ornament" style="left:134px; top:566px; height:62px;"></div>
    <div class="ornament" role="img" aria-label="Brown swirl flourish ornament" style="left:384px; top:566px; height:62px;"></div>
    <div class="band" style="left:131px; top:629px; width:382px; height:32px;"></div>
    <div class="weight" style="left:131px; top:660px;">30g</div>
  </section>

  <!-- Back of wrapper -->
  <section class="wrapper-back">
    <div class="band" style="left:687px; top:128px; width:382px; height:45px;"></div>
    <div class="ornament" role="img" aria-label="Brown swirl flourish ornament" style="left:740px; top:173px; height:48px;"></div>
    <div class="ornament" role="img" aria-label="Brown swirl flourish ornament" style="left:929px; top:173px; height:48px;"></div>

    <div class="brand-name" style="left:687px; top:270px; font-size:72px;">Celvano</div>
    <div class="tagline" style="left:718px; top:352px;">Quality Chocolate Store</div>

    <div class="flavour" style="left:687px; top:408px; font-size:34px;">plain dark</div>
    <div class="product-word" style="left:790px; top:470px; font-size:46px;">chocolate</div>

    <div class="ornament" role="img" aria-label="Brown swirl flourish ornament" style="left:740px; top:561px; height:58px;"></div>
    <div class="ornament" role="img" aria-label="Brown swirl flourish ornament" style="left:929px; top:561px; height:58px;"></div>
    <div class="band" style="left:687px; top:619px; width:382px; height:43px;"></div>
  </section>

  <div class="side-label" style="left:189px;">Front Side</div>
  <div class="side-label" style="left:758px;">Back Side</div>
</main>
</body>
</html>
```